Cat Toy Box Design

We are looking to design our packaging for our cat toy. The box is a
6.75 inches x 6.75 inches x 11.75 inches.

The images I've uploaded is from a sample box - We will need to add our logo to it. I have also attached our logo.

```html
<!DOCTYPE html>
<html lang="en">
<head>
<meta charset="utf-8">
<title>Scratching Perch – Packaging</title>
<link rel="stylesheet" href="https://fonts.googleapis.com/css2?family=Righteous&family=Oswald:wght@500;700&family=Roboto+Condensed:wght@400&display=swap">
<style>
  :root{
    --orange-light:#f4b987;
    --orange-mid:#e27a47;
    --orange-deep:#c8411a;
    --brown:#a8471f;
    --brown-dark:#5a1a10;
    --ink:#3a1a0e;
    --white:#fbf7f4;
    --grey:#6f6f6f;
    --jute:#b08a55;
    --canvas:#ecebe8;
  }
  *{box-sizing:border-box;margin:0;padding:0}
  html,body{width:870px;height:1200px;overflow:hidden;background:var(--canvas)}
  .box-net{position:relative;width:870px;height:1200px}
  .panel{position:absolute;overflow:hidden;
    background:linear-gradient(180deg,var(--orange-light) 0%,var(--orange-mid) 55%,var(--orange-deep) 100%)}
  .panel .blob{position:absolute;border-radius:50%;background:rgba(255,230,205,.28)}
  .panel--top{left:435px;top:4px;width:435px;height:435px;
    background:linear-gradient(180deg,#e9a672 0%,var(--orange-light) 100%)}
  .panel--side{left:0;top:439px;width:435px;height:757px;border-right:1px solid rgba(90,26,16,.25)}
  .panel--front{left:435px;top:439px;width:435px;height:757px}

  .brand{position:absolute;display:flex;align-items:center;gap:10px;
    font-family:"Righteous",sans-serif;color:var(--brown-dark)}
  .brand__dot{width:34px;height:34px;border-radius:50%;background:var(--brown)}
  .brand__name{font-size:26px}

  .title{position:absolute;font-family:"Righteous",sans-serif;color:var(--white);
    -webkit-text-stroke:2px var(--brown-dark);text-shadow:4px 4px 0 var(--brown-dark);line-height:1;white-space:nowrap}

  .product-photo{position:absolute;border-radius:18px;
    background:radial-gradient(ellipse at 50% 40%,#d8c3a0 0%,#9a9a9a 70%,#7b7b7b 100%);
    border:6px solid var(--white)}

  .description{position:absolute;left:26px;top:28px;width:383px;
    font-family:"Roboto Condensed",sans-serif;font-size:16px;line-height:1.5;color:var(--ink);text-align:justify}

  .thumb{position:absolute;border-radius:14px;border:3px solid var(--white);background:#8c8c8c}
  .thumb--ball{background:linear-gradient(180deg,#e8e3dc,#b48a55)}
  .label{position:absolute;font-family:"Oswald",sans-serif;font-weight:700;color:var(--ink);font-size:13px;text-align:center}
  .assemble{position:absolute;font-family:"Oswald",sans-serif;font-weight:700;color:var(--ink);text-align:right}
  .assemble__head{font-size:22px}
  .assemble__sub{font-size:17px;font-weight:500}
  .hardware{position:absolute;border-radius:12px;border:3px solid var(--white);
    background:linear-gradient(135deg,#f2f2f2,#b9b9b9)}
</style>
</head>
<body>
<main class="box-net">

  <!-- Top flap -->
  <section class="panel panel--top">
    <div class="blob" style="left:180px;top:-60px;width:320px;height:220px"></div>
    <div class="brand" style="left:40px;top:50px">
      <span class="brand__dot"></span><span class="brand__name">Tallpaw Goods</span>
    </div>
    <div class="title" style="left:40px;top:170px;font-size:46px">SCRATCHING</div>
    <div class="title" style="left:40px;top:228px;font-size:90px">PERCH</div>
  </section>

  <!-- Side panel -->
  <section class="panel panel--side">
    <div class="blob" style="left:200px;top:520px;width:320px;height:320px"></div>
    <p class="description">Scratching post provides a place for cats to sharpen their claws and keep nails healthy. Includes a single pillar scratching post with a replacable dangle toy. Natural jute fiber offers an optimal scratching surface. Sturdy base helps prevent the post from tipping. Ideal for redirecting cats away from scratching household carpet or furniture.</p>

    <div class="product-photo" role="img" aria-label="Scratching perch with grey carpet top and base, jute-wrapped post and dangling ball" style="left:26px;top:262px;width:250px;height:300px"></div>

    <div class="thumb" role="img" aria-label="Close-up of soft grey carpet base" style="left:300px;top:270px;width:100px;height:105px"></div>
    <div class="label" style="left:300px;top:380px;width:100px">Soft Base</div>
    <div class="thumb thumb--ball" role="img" aria-label="Close-up of dangling jute ball toy" style="left:300px;top:410px;width:100px;height:105px"></div>
    <div class="label" style="left:300px;top:520px;width:100px">Dangling Ball</div>

    <div class="assemble" style="right:26px;top:575px">
      <div class="assemble__head">EASY TO ASSEMBLE</div>
      <div class="assemble__sub">Set Screws</div>
    </div>

    <div class="hardware" role="img" aria-label="Allen key" style="left:26px;top:625px;width:80px;height:52px"></div>
    <div class="hardware" role="img" aria-label="Threaded rod" style="left:116px;top:625px;width:80px;height:52px"></div>
    <div class="hardware" role="img" aria-label="Long screw" style="left:26px;top:687px;width:80px;height:52px"></div>
    <div class="hardware" role="img" aria-label="Bolt" style="left:116px;top:687px;width:80px;height:52px"></div>
    <div class="hardware" role="img" aria-label="Metal washer" style="left:206px;top:640px;width:80px;height:90px"></div>
  </section>

  <!-- Front panel -->
  <section class="panel panel--front">
    <div class="blob" style="left:230px;top:-40px;width:300px;height:260px"></div>
    <div class="blob" style="left:-80px;top:560px;width:260px;height:260px"></div>
    <div class="brand" style="left:30px;top:34px">
      <span class="brand__dot"></span><span class="brand__name">Tallpaw Goods</span>
    </div>
    <div class="product-photo" role="img" aria-label="Scratching perch with grey carpet top and base, jute-wrapped post and dangling ball" style="left:40px;top:100px;width:360px;height:460px"></div>
    <div class="title" style="left:28px;top:585px;font-size:54px">SCRATCHING</div>
    <div class="title" style="left:24px;top:640px;font-size:104px">PERCH</div>
  </section>

</main>
</body>
</html>
```